Business Card Design Graduates

Slogan
"Practical Skills + Theory = Paid Job"

We assist Accounting Graduates to get work at the end of their University Degree by offering them a 6 week practical experience program.

At completion of the program they get business cards in their own Name, Title, phone numbers, address and email address. So, I need to be able to have a template where I can change these details and purchase business cards via Cardoloom or other outside printers.

I want it to be a bit colourful... ie not a plain white background or black, some blue would be nice. But it also needs to look professional as they will be meeting with future employers and networking. We help them get a paid job in Accounting at completion of the 6 week program.

Target Market(s)

Students and Employers

Industry/Entity Type

Business

Contact Information for Business Card

Marietta Dombrowski, Director, PO Box 418, Kelworth NSW 2174, Phone: 9482-3107 Fax: 9482-5921 Email: mariettad@harrowquill.com.au Web: www.HarrowquillWorkStart.com.au

Requirements
Must have
• changeable fields for me to change details for each student who graduates. The name of the company is already in the logo so no need to duplicate the name. Look at the website www.HarrowquillWorkStart.com.au because we expect the design should match our Corporate Image.

```html
<!DOCTYPE html>
<html lang="en">
<head>
<meta charset="utf-8">
<title>Harrowquill WorkStart – Business Card</title>
<link href="https://fonts.googleapis.com/css2?family=Exo+2:wght@400;500;600;700&display=swap" rel="stylesheet">
<style>
  :root {
    --card-bg: #eef0f2;
    --card-bg-edge: #dfe3e6;
    --brand-blue: #1d4ea6;
    --brand-blue-dark: #163f8c;
    --accent-green: #7cc242;
    --footer-light: #f3f3f3;
    --footer-dark: #c9cbcd;
    --ink-dark: #333a40;
    --ink-white: #ffffff;
    --icon-ring: #dfe6f2;
    --social-grey: #4a4f55;
  }
  html, body {
    margin: 0;
    padding: 0;
    width: 1200px;
    height: 769px;
    overflow: hidden;
    background: #ffffff;
    font-family: "Exo 2", sans-serif;
  }
  .card {
    position: relative;
    width: 1200px;
    height: 769px;
    background: linear-gradient(135deg, var(--card-bg) 0%, #f7f8f9 50%, var(--card-bg-edge) 100%);
    overflow: hidden;
  }
  .brand {
    position: absolute;
    left: 318px;
    top: 105px;
    display: flex;
    align-items: center;
    gap: 22px;
  }
  .brand-mark {
    width: 58px;
    height: 58px;
    background: var(--accent-green);
  }
  .brand-name {
    font-size: 64px;
    font-weight: 500;
    color: var(--brand-blue);
    letter-spacing: 0.5px;
    white-space: nowrap;
  }
  .contact-band {
    position: absolute;
    left: 0;
    top: 274px;
    width: 1200px;
    height: 356px;
    background: linear-gradient(180deg, var(--brand-blue) 0%, var(--brand-blue-dark) 100%);
    border-top: 8px solid var(--accent-green);
    border-bottom: 8px solid var(--accent-green);
    box-sizing: border-box;
  }
  .contact-col {
    position: absolute;
    top: 70px;
    width: 360px;
    margin-left: -180px;
    text-align: center;
    color: var(--ink-white);
  }
  .col-person { left: 226px; }
  .col-web { left: 609px; }
  .col-phone { left: 985px; }
  .contact-icon {
    display: block;
    width: 108px;
    height: 108px;
    margin: 0 auto 36px;
  }
  .person-name {
    font-size: 50px;
    font-weight: 600;
    letter-spacing: 1px;
    line-height: 1;
    margin: 0;
  }
  .person-title {
    font-size: 17px;
    font-weight: 500;
    letter-spacing: 1.5px;
    margin: 8px 0 0;
  }
  .contact-line {
    font-size: 31px;
    font-weight: 400;
    letter-spacing: 0.8px;
    line-height: 42px;
    margin: 0;
  }
  .col-web .contact-icon,
  .col-phone .contact-icon { margin-bottom: 30px; }
  .social-footer {
    position: absolute;
    left: 0;
    top: 630px;
    width: 1200px;
    height: 139px;
    background: linear-gradient(90deg, var(--footer-light) 0%, #e4e5e6 45%, var(--footer-dark) 100%);
  }
  .follow-heading {
    position: absolute;
    left: 111px;
    top: 36px;
    margin: 0;
    font-size: 33px;
    font-weight: 500;
    color: var(--ink-dark);
    letter-spacing: 1.5px;
  }
  .follow-sub {
    position: absolute;
    left: 111px;
    top: 78px;
    margin: 0;
    font-size: 13px;
    font-weight: 500;
    color: var(--ink-dark);
    letter-spacing: 1px;
  }
  .social-list {
    position: absolute;
    left: 400px;
    top: 44px;
    display: flex;
    gap: 44px;
    margin: 0;
    padding: 0;
    list-style: none;
  }
  .social-slot {
    width: 38px;
    height: 38px;
    border-radius: 6px;
    background: var(--social-grey);
  }
</style>
</head>
<body>
  <main class="card">
    <header class="brand">
      <span class="brand-mark" aria-hidden="true"></span>
      <span class="brand-name">Harrowquill WorkStart</span>
    </header>

    <section class="contact-band">
      <div class="contact-col col-person">
        <svg class="contact-icon" viewBox="0 0 108 108" aria-hidden="true">
          <circle cx="54" cy="54" r="52" fill="var(--icon-ring)"/>
          <circle cx="54" cy="54" r="42" fill="var(--brand-blue)"/>
          <circle cx="54" cy="42" r="13" fill="#ffffff"/>
          <path d="M30 76 C30 60 42 57 54 57 C66 57 78 60 78 76 Z" fill="#ffffff"/>
        </svg>
        <p class="person-name">OWEN CASTELL</p>
        <p class="person-title">GENERAL MANAGER</p>
      </div>

      <div class="contact-col col-web">
        <svg class="contact-icon" viewBox="0 0 108 108" aria-hidden="true">
          <circle cx="54" cy="54" r="52" fill="var(--icon-ring)"/>
          <circle cx="54" cy="54" r="42" fill="var(--brand-blue)"/>
          <g fill="none" stroke="#ffffff" stroke-width="3">
            <circle cx="54" cy="54" r="24"/>
            <ellipse cx="54" cy="54" rx="11" ry="24"/>
            <line x1="30" y1="54" x2="78" y2="54"/>
            <path d="M34 42 H74 M34 66 H74"/>
            <line x1="54" y1="30" x2="54" y2="78"/>
          </g>
        </svg>
        <p class="contact-line">urname@inbox.net</p>
        <p class="contact-line">www.urwebpage.net</p>
      </div>

      <div class="contact-col col-phone">
        <svg class="contact-icon" viewBox="0 0 108 108" aria-hidden="true">
          <circle cx="54" cy="54" r="52" fill="var(--icon-ring)"/>
          <circle cx="54" cy="54" r="42" fill="var(--brand-blue)"/>
          <rect x="41" y="28" width="26" height="50" rx="4" fill="#ffffff"/>
          <rect x="45" y="34" width="18" height="33" fill="var(--brand-blue)"/>
          <circle cx="54" cy="72" r="2.5" fill="var(--brand-blue)"/>
        </svg>
        <p class="contact-line">012 555 0142</p>
        <p class="contact-line">012 555 0142</p>
      </div>
    </section>

    <footer class="social-footer">
      <p class="follow-heading">FOLLOW US</p>
      <p class="follow-sub">ON SOCIAL NETWORKS</p>
      <ul class="social-list" aria-label="Social network links">
        <li class="social-slot"></li>
        <li class="social-slot"></li>
        <li class="social-slot"></li>
        <li class="social-slot"></li>
      </ul>
    </footer>
  </main>
</body>
</html>
```